" A empresa está localizada numa cidade pequena, porém muito próximos da capital do estado de Minas Gerais e de outras cidades maiores do interior. Considerada região metropolitana da capital. Criaremos um site e faremos venda de produtos na loja virtual, bem como marcação de serviços. Queremos trazer profissionalismo e um serviço diferenciado para a região. Nossa meta é em 3 anos ser a principal referência nesse serviço num raio de 50 km da cidade. "

```html
<!DOCTYPE html>
<html lang="pt-BR">
<head>
<meta charset="UTF-8">
<title>Folha Clara — Adesivo</title>
<link rel="stylesheet" href="https://fonts.googleapis.com/css2?family=Cinzel:wght@400&family=Cormorant+Garamond:wght@400&family=Comfortaa:wght@400&display=swap">
<style>
  :root {
    --backdrop: #ececec;
    --mint: #8ecfbe;
    --mint-deep: #7fc3b1;
    --rim: #d8efe8;
    --gold: #ddd0a8;
    --gold-line: #e6dcbd;
  }
  * { margin: 0; padding: 0; box-sizing: border-box; }
  html, body {
    width: 1200px;
    height: 1200px;
    overflow: hidden;
    background: var(--backdrop);
  }
  .canvas {
    position: relative;
    width: 1200px;
    height: 1200px;
  }
  .sticker {
    position: absolute;
    left: 0;
    top: 0;
    width: 1200px;
    height: 1200px;
  }
  .brand-mark {
    position: absolute;
    left: 566px;
    top: 350px;
    width: 68px;
    height: 68px;
    border-radius: 50%;
    background: var(--gold);
  }
  .brand-name {
    position: absolute;
    left: 0;
    width: 1200px;
    top: 500px;
    text-align: center;
    font-family: "Cinzel", serif;
    font-weight: 400;
    font-size: 92px;
    line-height: 1;
    letter-spacing: 2px;
    color: var(--gold);
  }
  .tagline {
    position: absolute;
    left: 0;
    width: 1200px;
    top: 592px;
    text-align: center;
    font-family: "Cormorant Garamond", serif;
    font-size: 30px;
    line-height: 1;
    letter-spacing: 4px;
    color: var(--gold);
  }
  .contact {
    position: absolute;
    left: 0;
    width: 1200px;
    top: 720px;
    display: flex;
    justify-content: center;
    align-items: center;
    gap: 18px;
  }
  .contact-icon { width: 58px; height: 58px; }
  .contact-phone {
    font-family: "Comfortaa", sans-serif;
    font-size: 34px;
    letter-spacing: 1px;
    color: var(--gold);
  }
</style>
</head>
<body>
  <main class="canvas">
    <svg class="sticker" viewBox="0 0 1200 1200" aria-hidden="true">
      <circle cx="600" cy="600" r="412" fill="var(--rim)"/>
      <circle cx="600" cy="600" r="402" fill="var(--mint)"/>
      <circle cx="600" cy="600" r="384" fill="none" stroke="var(--gold-line)" stroke-width="4"/>
    </svg>

    <span class="brand-mark" aria-hidden="true"></span>
    <h1 class="brand-name">FOLHA CLARA</h1>
    <p class="tagline">CUIDADO QUE REALÇA</p>

    <div class="contact">
      <svg class="contact-icon" viewBox="0 0 58 58" aria-hidden="true">
        <circle cx="29" cy="29" r="28" fill="var(--gold)"/>
        <path d="M20 14c2-1 4 0 5 2l3 6c1 2 0 3-1 4l-2 2c2 4 5 7 9 9l2-2c1-1 2-2 4-1l6 3c2 1 3 3 2 5l-2 4c-1 2-3 3-6 2C28 45 16 33 13 21c-1-3 0-5 2-6z" fill="var(--mint-deep)"/>
      </svg>
      <span class="contact-phone">(31) 9 9000-4821</span>
    </div>
  </main>
</body>
</html>
```